Custom Manufacturing Company square space website design

I own a custom manufacturing company that uses precision cutting technology to manufacture project components over a couple industries. We have an industrial CNC router and state of the art edge bander and cut a lot of cabinetry components for cabinet shops, builders, closet companies, ect. We offer design and assembly for any cabinetry or can build cabinets to spec. We also cut components for other industries out of wood, plastics, acryclics, ect. We offer design engineering services, product development protype services. we have a 3D printer farm. We want our communicate trust, dependability, and the value we place on client relationships.

We essentially want a credibility website. Landing page and drops downs for services we offer, capabilites, about us, contact

```html
<!DOCTYPE html>
<html lang="en">
<head>
<meta charset="utf-8">
<title>Northline CNC — Custom Manufacturing</title>
<link rel="stylesheet" href="https://fonts.googleapis.com/css2?family=Michroma&family=Poppins:wght@400;500;600&family=Syncopate:wght@400;700&display=swap">
<style>
:root{
  --ink:#111111;
  --dark:#0d0e0d;
  --paper:#ffffff;
  --panel:#f2f2f2;
  --muted:#444444;
  --btn:#333333;
  --light-text:#d9d9d9;
  --wide:"Syncopate","Michroma",sans-serif;
}
*{margin:0;padding:0;box-sizing:border-box}
html,body{width:1200px;height:4498px;overflow:hidden;background:var(--paper);color:var(--ink);font-family:"Poppins",sans-serif}
.page{position:relative;width:1200px;height:4498px}
.abs{position:absolute}
.display{font-family:var(--wide);font-weight:700;letter-spacing:2px;line-height:1.18}
.smallcaps{font-family:var(--wide);font-weight:700;letter-spacing:1px}
.body-copy{font-size:14.5px;line-height:24px;color:var(--muted)}
.btn{display:inline-block;background:var(--btn);color:#fff;font-family:var(--wide);font-weight:700;font-size:13px;letter-spacing:1px;padding:0 14px;height:44px;line-height:44px;white-space:nowrap}
.photo{position:absolute}

/* header */
.header{position:absolute;left:0;top:0;width:1200px;height:105px;background:#fff}
.brand{position:absolute;left:70px;top:14px;width:160px;text-align:center}
.brand-mark{display:block;margin:0 auto 8px;width:60px;height:44px;border:2px solid #222}
.brand-name{font-family:var(--wide);font-weight:700;font-size:13px;letter-spacing:1px;color:#222;white-space:nowrap}
.nav{position:absolute;right:73px;top:46px;display:flex;gap:26px;font-family:var(--wide);font-weight:700;font-size:11.5px;letter-spacing:1px;color:#333;white-space:nowrap}

/* hero */
.hero{position:absolute;left:0;top:105px;width:1200px;height:632px;background:linear-gradient(180deg,#4a4a44 0%,#8c8577 45%,#c9bfae 100%)}
.hero-title{position:absolute;left:73px;top:205px;color:#fff;font-size:46px;white-space:nowrap}
.hero-text{position:absolute;left:73px;top:268px;width:560px;color:#fff;font-weight:600;font-size:18px;line-height:28px}
.hero .btn{position:absolute;left:73px;top:370px;background:#111}
.dots{position:absolute;left:549px;top:583px;display:flex;gap:12px}
.dots span{width:28px;height:4px;background:#fff}
.dots span+span{background:#222}

/* dark sections */
.dark{position:absolute;left:0;width:1200px;background:var(--dark);color:#fff}
.dark h2{position:absolute;left:0;width:1200px;text-align:center;font-size:36px;white-space:nowrap}
.dark .lead{position:absolute;left:130px;width:940px;text-align:center;font-size:14.5px;line-height:27px;color:var(--light-text)}
.card{position:absolute;width:329px}
.card .photo{position:relative;width:329px;height:197px}
.card h3{margin-top:24px;font-size:19px;white-space:nowrap}
.card p{margin-top:10px;font-size:13px;line-height:24px;color:var(--light-text)}

/* footer */
.footer{position:absolute;left:0;top:4170px;width:1200px;height:328px;background:var(--dark);color:#fff}
.footer h4{font-family:var(--wide);font-weight:700;font-size:13px;letter-spacing:1px;margin-bottom:18px;white-space:nowrap}
.footer ul{list-style:none;font-size:13px;line-height:36px}
.fcol{position:absolute;top:60px}
.contact li{display:flex;gap:12px;line-height:22px;margin-bottom:14px}
.contact svg{flex:none;margin-top:4px}
.social{display:flex;gap:14px;justify-content:center;margin-top:14px}
.social span{width:16px;height:16px;border-radius:50%;background:#fff}
.fine{font-size:11.5px;line-height:24px;text-align:center;margin-top:14px}
</style>
</head>
<body>
<div class="page">

<header class="header">
  <div class="brand">
    <span class="brand-mark"></span>
    <div class="brand-name">NORTHLINE CNC</div>
  </div>
  <nav class="nav"><span>HOME</span><span>SERVICES WE OFFER</span><span>CAPABILITIES</span><span>ABOUT US</span><span>CONTACT</span></nav>
</header>

<section class="hero" role="img" aria-label="Green industrial CNC router head cutting shapes from a white sheet">
  <h1 class="display hero-title">NORTHLINE CNC</h1>
  <p class="hero-text">We own a custom manufacturing company that uses precision cutting technology to manufacture project components over a couple industries.</p>
  <span class="btn">Read More</span>
  <div class="dots"><span></span><span></span><span></span></div>
</section>

<section>
  <div class="abs" style="left:496px;top:805px;width:631px;height:430px;background:var(--panel)"></div>
  <div class="photo" style="left:73px;top:851px;width:514px;height:435px;background:linear-gradient(135deg,#7a8a96,#b7a58f 55%,#d8d3cb)" role="img" aria-label="Craftsman in apron at a CNC machine in a workshop"></div>
  <div class="abs" style="left:620px;top:845px;width:480px">
    <h2 class="display" style="font-size:35px">WELCOME TO<br>NORTHLINE CNC</h2>
    <p class="body-copy" style="margin-top:22px">Nemo enim ipsam voluptatem quia voluptas sit aspernatur aut odit aut fugit, sed quia consequuntur magni dolores eos qui ratione voluptatem sequi nesciunt..</p>
    <p class="body-copy" style="margin-top:10px">Neque porro quisquam est, qui dolorem ipsum quia dolor sit amet, consectetur, adipisci velit, sed quia non numquam eius modi tempora incidunt ut labore et dolore magnam aliquam quaerat voluptatem.</p>
    <span class="btn" style="margin-top:22px">Read More</span>
  </div>
</section>

<section class="dark" style="top:1349px;height:613px">
  <h2 class="display" style="top:78px">CABINETRY COMPONENTS</h2>
  <p class="lead" style="top:132px">Nemo enim ipsam voluptatem quia voluptas sit aspernatur aut odit aut fugit, sed quia consequuntur magni dolores eos qui ratione voluptatem sequi nesciunt..</p>
  <div class="card" style="left:73px;top:215px">
    <div class="photo" style="background:linear-gradient(135deg,#e8e3dc,#d9b9ad 50%,#b8a99b)" role="img" aria-label="Woman choosing cabinet door samples in a showroom"></div>
    <h3 class="smallcaps">Cabinet Shops</h3>
    <p>Sed ut perspiciatis unde omnis iste natus error sit voluptatem accusantium doloremque sint occaecat cupidatat non proident.</p>
  </div>
  <div class="card" style="left:435px;top:215px">
    <div class="photo" style="background:linear-gradient(180deg,#cfd2d4,#b9b5ad 60%,#7f807d)" role="img" aria-label="Office interior with built-in filing cabinets"></div>
    <h3 class="smallcaps">Builders</h3>
    <p>Sed ut perspiciatis unde omnis iste natus error sit voluptatem accusantium doloremque sint occaecat cupidatat non proident.</p>
  </div>
  <div class="card" style="left:797px;top:215px">
    <div class="photo" style="background:linear-gradient(135deg,#d9c9c0,#f1ece6 50%,#c7898f)" role="img" aria-label="Closet system with shelves, drawers and hanging clothes"></div>
    <h3 class="smallcaps">Closet Companies</h3>
    <p>Sed ut perspiciatis unde omnis iste natus error sit voluptatem accusantium doloremque sint occaecat cupidatat non proident.</p>
  </div>
</section>

<section>
  <div class="photo" style="left:73px;top:2040px;width:527px;height:406px;background:linear-gradient(135deg,#5c5048,#9a6b4d 45%,#d9cfc3)" role="img" aria-label="Engineer in plaid shirt marking a board in a workshop"></div>
  <div class="abs" style="left:632px;top:2098px;width:480px">
    <h2 class="display" style="font-size:35px">DESIGN<br>ENGINEERING</h2>
    <p class="body-copy" style="margin-top:22px">Neque porro quisquam est, qui dolorem ipsum quia dolor sit amet, consectetur, adipisci velit, sed quia non numquam eius modi tempora incidunt ut labore et dolore magnam aliquam quaerat voluptatem.</p>
    <span class="btn" style="margin-top:22px">Read More</span>
  </div>
  <div class="abs" style="left:73px;top:2486px;width:500px">
    <h2 class="display" style="font-size:35px">PRODUCT<br>DEVELOPMENT<br>PROTOTYPE</h2>
    <p class="body-copy" style="margin-top:22px">Neque porro quisquam est, qui dolorem ipsum quia dolor sit amet, consectetur, adipisci velit, sed quia non numquam eius modi tempora incidunt ut labore et dolore magnam aliquam quaerat voluptatem.</p>
    <span class="btn" style="margin-top:22px">Read More</span>
  </div>
  <div class="photo" style="left:601px;top:2448px;width:526px;height:405px;background:linear-gradient(180deg,#6e5e4c,#b59a78 45%,#d2b895)" role="img" aria-label="Close-up of a routed MDF panel with sawdust"></div>
</section>

<section class="dark" style="top:2931px;height:615px">
  <h2 class="display" style="top:85px">CUT COMPONENTS INDUSTRIES</h2>
  <p class="lead" style="top:140px">Nemo enim ipsam voluptatem quia voluptas sit aspernatur aut odit aut fugit, sed quia consequuntur magni dolores eos qui ratione voluptatem sequi nesciunt..</p>
  <div class="card" style="left:73px;top:217px">
    <div class="photo" style="background:linear-gradient(135deg,#8a8a8a,#c9a676 50%,#3c4a8a)" role="img" aria-label="CNC spindle cutting a wooden board"></div>
    <h3 class="smallcaps">Wood Cutting</h3>
    <p>Sed ut perspiciatis unde omnis iste natus error sit voluptatem accusantium doloremque sint occaecat cupidatat non proident.</p>
  </div>
  <div class="card" style="left:435px;top:217px">
    <div class="photo" style="background:linear-gradient(180deg,#6d7073,#c5c8cb 55%,#8e9194)" role="img" aria-label="Milling tool cutting a plastic sheet"></div>
    <h3 class="smallcaps">Plastics Cutting</h3>
    <p>Sed ut perspiciatis unde omnis iste natus error sit voluptatem accusantium doloremque sint occaecat cupidatat non proident.</p>
  </div>
  <div class="card" style="left:797px;top:217px">
    <div class="photo" style="background:linear-gradient(180deg,#2a3550,#2f61b5 55%,#6fa4e8)" role="img" aria-label="Laser cutting a blue acrylic sheet"></div>
    <h3 class="smallcaps">Acrylics Cutting</h3>
    <p>Sed ut perspiciatis unde omnis iste natus error sit voluptatem accusantium doloremque sint occaecat cupidatat non proident.</p>
  </div>
</section>

<section>
  <div class="abs" style="left:496px;top:3616px;width:631px;height:500px;background:var(--panel)"></div>
  <div class="photo" style="left:73px;top:3662px;width:514px;height:435px;background:linear-gradient(90deg,#3f4652,#a9adb3 50%,#c0522e)" role="img" aria-label="Industrial 3D printer in a workshop"></div>
  <div class="abs" style="left:620px;top:3666px;width:480px">
    <h2 class="display" style="font-size:35px">3D PRINTER<br>FARM</h2>
    <p class="body-copy" style="margin-top:22px">Nemo enim ipsam voluptatem quia voluptas sit aspernatur aut odit aut fugit, sed quia consequuntur magni dolores eos qui ratione voluptatem sequi nesciunt..</p>
    <p class="body-copy" style="margin-top:10px">Neque porro quisquam est, qui dolorem ipsum quia dolor sit amet, consectetur, adipisci velit, sed quia non numquam eius modi tempora incidunt ut labore et dolore magnam aliquam quaerat voluptatem.</p>
    <span class="btn" style="margin-top:22px">Read More</span>
  </div>
</section>

<footer class="footer">
  <div class="fcol" style="left:75px;top:56px;width:200px;text-align:center">
    <span class="brand-mark" style="border-color:#fff"></span>
    <div class="brand-name" style="color:#fff">NORTHLINE CNC</div>
    <div class="social" aria-label="Social media links"><span></span><span></span><span></span><span></span><span></span></div>
    <p class="fine">Copyright © 2023 Company Name<br>All Rights Reserved</p>
  </div>
  <div class="fcol" style="left:342px">
    <h4>SITE MAP</h4>
    <ul><li>Home</li><li>Services We Offer</li><li>Capabilities</li><li>About us</li><li>Contact</li></ul>
  </div>
  <div class="fcol" style="left:566px">
    <h4>CAPABILITIES</h4>
    <ul><li>Quis autem</li><li>Eum iure reprehen</li><li>Derit qui in</li><li>Eavoluptate</li></ul>
  </div>
  <div class="fcol" style="left:832px;width:300px">
    <h4>CONTACT US</h4>
    <ul class="contact">
      <li><svg width="14" height="14" viewBox="0 0 14 14"><path d="M2 1v12M2 2h9l-2 3 2 3H2" fill="#fff" stroke="#fff" stroke-width="1.5"/></svg><span>Excepteur sint occaecat<br>cupidatat non</span></li>
      <li><svg width="14" height="14" viewBox="0 0 14 14"><path d="M3 1l3 3-2 2c1 2 2 3 4 4l2-2 3 3-2 2C6 13 1 8 1 3z" fill="#fff"/></svg><span>1-555-014-2736</span></li>
      <li><svg width="14" height="14" viewBox="0 0 14 14"><rect x="1" y="3" width="12" height="8" fill="#fff"/><path d="M1 3l6 5 6-5" fill="none" stroke="#0d0e0d" stroke-width="1.2"/></svg><span>info@northlinecnc.com</span></li>
    </ul>
  </div>
</footer>

</div>
</body>
</html>
```